We need a web design for a retail food business based in Greater Western Sydney Australia called Golden Lantern Chinese Restaurant. Basically just need a simple yet easily to navigate website to browse through a menu, gallery , brief description about us, opening hours.
Menu and Gallery will be constantly updated.
Will provide own images for gallery
Updates
Menu has been uploaded and some idea on the colours I would like on the site
Some additional pictures added to see what designs you guys can come up with . Thanks again
To All Designers,
Any extra fee on top of the designs that feels need to be charged, please let me know in advance
Reason: Extending Deadline as I have yet to find a design that I would like...Thanks guys
Target Market(s)
All groups
Industry/Entity Type
Business
Requirements
Must have
- Open minded to any designs
Nice to have
- Would like slideshow behind main logo.
Preferred light coloured site yet not too playful
Should not have
- Preferably no dark colours backgrounds

```html
<!DOCTYPE html>
<html lang="en">
<head>
<meta charset="utf-8">
<title>Golden Lantern Chinese Restaurant</title>
<link rel="stylesheet" href="https://fonts.googleapis.com/css2?family=Ubuntu:wght@300;400;500&family=Open+Sans:wght@400;600&display=swap">
<style>
  :root {
    --page: #f2f0f0;
    --red: #a80d0d;
    --red-bright: #c81414;
    --red-deep: #860000;
    --ink: #333333;
    --muted: #5a5a5a;
    --soft: #9a9a9a;
    --rule: #d2d0d0;
  }
  * { box-sizing: border-box; margin: 0; padding: 0; }
  html, body { width: 1200px; height: 1100px; overflow: hidden; }
  body { background: var(--page); font-family: "Open Sans", sans-serif; color: var(--ink); position: relative; }
  .site-top-line { position: absolute; left: 0; top: 0; width: 1200px; height: 3px; background: #111; }

  .brand { position: absolute; left: 120px; top: 26px; width: 260px; height: 110px; }
  .brand-mark { position: absolute; left: 86px; top: 0; width: 78px; height: 78px; border-radius: 50%; background: var(--red); }
  .brand-name { position: absolute; left: 0; top: 80px; width: 260px; font-family: "Ubuntu", sans-serif; font-weight: 500; font-size: 27px; letter-spacing: 1px; color: #3a3a3a; text-transform: uppercase; white-space: nowrap; }

  .contact { position: absolute; right: 120px; top: 16px; text-align: right; }
  .contact-address { font-size: 13px; line-height: 17px; color: var(--ink); text-transform: uppercase; }
  .contact-phone { margin-top: 12px; font-size: 17px; color: var(--red); }

  .main-nav { position: absolute; left: 446px; top: 90px; width: 754px; height: 45px; border-radius: 22px 0 0 22px; background: linear-gradient(#bb1212, var(--red-deep)); }
  .main-nav a { position: absolute; top: 14px; font-family: "Ubuntu", sans-serif; font-weight: 500; font-size: 13.5px; color: #fff; text-decoration: none; text-transform: uppercase; white-space: nowrap; }

  .hero { position: absolute; left: 0; top: 159px; width: 1200px; height: 484px; background: radial-gradient(ellipse at 50% 35%, #b4472e 0%, #6e2218 45%, #2a1a18 100%); }
  .hero-arrow { position: absolute; top: 222px; width: 28px; height: 32px; background: rgba(230,230,230,.75); }
  .hero-arrow.prev { left: 0; border-radius: 0 4px 4px 0; }
  .hero-arrow.next { right: 0; border-radius: 4px 0 0 4px; }
  .hero-arrow svg { position: absolute; left: 8px; top: 9px; }
  .hero-caption { position: absolute; left: 282px; top: 330px; width: 632px; height: 92px; border-radius: 4px; background: rgba(255,255,255,.78); }
  .hero-title { position: absolute; left: 16px; top: 12px; font-family: "Ubuntu", sans-serif; font-weight: 500; font-size: 17px; letter-spacing: -0.3px; color: var(--red); text-transform: uppercase; }
  .hero-text { position: absolute; left: 16px; top: 42px; width: 496px; font-size: 12.5px; line-height: 17px; letter-spacing: -0.2px; color: var(--ink); }
  .btn { display: block; position: absolute; background: linear-gradient(var(--red-bright), var(--red-deep)); color: #fff; font-family: "Ubuntu", sans-serif; font-weight: 500; text-transform: uppercase; text-decoration: none; text-align: center; border-radius: 2px; white-space: nowrap; }
  .hero-caption .btn { left: 519px; top: 45px; width: 101px; height: 34px; line-height: 34px; font-size: 14px; }
  .hero-dots { position: absolute; left: 540px; top: 456px; width: 125px; height: 28px; border-radius: 5px 5px 0 0; background: #e8e6e6; }
  .hero-dots span { position: absolute; top: 8px; width: 12px; height: 12px; border-radius: 50%; background: #9a9a9a; }
  .hero-dots span.active { background: #111; }

  .promo { position: absolute; top: 659px; width: 470px; height: 88px; background: linear-gradient(#cf1717, #8f0202); color: #fff; font-family: "Ubuntu", sans-serif; font-weight: 300; text-transform: uppercase; text-align: center; white-space: nowrap; overflow: hidden; }
  .promo-photo { position: absolute; left: 5px; top: 5px; width: 100px; height: 78px; background: linear-gradient(135deg, #f3f0ea 0%, #c9692e 55%, #8a3411 100%); }
  .promo-body { position: absolute; left: 110px; right: 8px; }
  .promo-head { font-size: 33px; line-height: 38px; }
  .promo-sub { font-size: 17px; line-height: 22px; }
  .promo-note { font-size: 12px; line-height: 16px; font-weight: 400; }

  .section-title { position: absolute; top: 773px; font-family: "Ubuntu", sans-serif; font-weight: 400; font-size: 17px; color: var(--muted); text-transform: uppercase; }
  .section-title em { font-style: normal; color: var(--red); }
  .welcome-photo { position: absolute; left: 120px; top: 818px; width: 240px; height: 152px; background: radial-gradient(ellipse at 35% 55%, #8a2310 0%, #b44a1e 40%, #bcd07a 100%); }
  .welcome-text { position: absolute; left: 370px; top: 814px; width: 380px; font-size: 10.5px; line-height: 14.5px; letter-spacing: -0.1px; color: var(--muted); text-align: justify; }
  .welcome-text p + p { margin-top: 14px; }
  .menu-photo { position: absolute; left: 780px; top: 819px; width: 300px; height: 105px; background: linear-gradient(100deg, #c4521f 0%, #e07a2a 45%, #7a8a3a 75%, #3b5a23 100%); }
  .menu-text { position: absolute; left: 780px; top: 939px; width: 212px; font-size: 10.5px; line-height: 14.5px; color: var(--muted); }
  .menu-teaser .btn { left: 1000px; top: 941px; width: 80px; height: 28px; line-height: 28px; font-size: 12px; }

  .footer-rule { position: absolute; left: 120px; top: 1010px; width: 960px; height: 1px; background: var(--rule); }
  .copyright { position: absolute; left: 120px; top: 1040px; font-family: Arial, sans-serif; font-size: 12px; color: var(--soft); }
  .social { position: absolute; top: 1031px; width: 28px; height: 28px; border-radius: 50%; background: #2e2e2e; }
</style>
</head>
<body>
  <div class="site-top-line"></div>

  <header>
    <div class="brand">
      <div class="brand-mark"></div>
      <div class="brand-name">Golden Lantern</div>
    </div>
    <div class="contact">
      <div class="contact-address">Shop 7, 22-26 Harbour Lane,<br>Kingsvale NSW 2761</div>
      <div class="contact-phone">PHONE: (02) 4555 0182</div>
    </div>
    <nav class="main-nav">
      <a href="#" style="left:26px">Home</a>
      <a href="#" style="left:108px">Menu</a>
      <a href="#" style="left:189px">Gallery</a>
      <a href="#" style="left:288px">About Us</a>
      <a href="#" style="left:395px">Opening Hours</a>
      <a href="#" style="left:544px">Contact Us</a>
    </nav>
  </header>

  <section class="hero" role="img" aria-label="Slideshow photo of the restaurant dining room with red walls and set tables">
    <div class="hero-arrow prev"><svg width="12" height="14" viewBox="0 0 12 14"><path d="M9 1 L3 7 L9 13" fill="none" stroke="#fff" stroke-width="3"/></svg></div>
    <div class="hero-arrow next"><svg width="12" height="14" viewBox="0 0 12 14"><path d="M3 1 L9 7 L3 13" fill="none" stroke="#fff" stroke-width="3"/></svg></div>
    <div class="hero-caption">
      <div class="hero-title">This is a fancy title</div>
      <div class="hero-text">Lorem ipsum dolor sit amet, consectetuer adipiscing elit, sed diam nonummy nibh euismod tincidunt ut laoreet dolore magna aliquam erat volutpat.</div>
      <a class="btn" href="#">View Menu</a>
    </div>
    <div class="hero-dots">
      <span style="left:8px"></span><span style="left:27px"></span><span class="active" style="left:46px"></span><span style="left:65px"></span><span style="left:84px"></span><span style="left:104px"></span>
    </div>
  </section>

  <div class="promo" style="left:120px">
    <div class="promo-photo" role="img" aria-label="Photo of chicken wings with dipping sauce"></div>
    <div class="promo-body" style="top:10px">
      <div class="promo-head">Order over $22,</div>
      <div class="promo-sub" style="margin-top:13px">Receive 6 mini rolls or 6 chicken wings</div>
    </div>
  </div>
  <div class="promo" style="left:610px">
    <div class="promo-photo" role="img" aria-label="Photo of chicken wings with dipping sauce"></div>
    <div class="promo-body" style="top:4px">
      <div class="promo-head" style="font-size:29px;line-height:34px">Order over $40</div>
      <div class="promo-sub" style="font-size:18px">Receive any dish to the value of $10</div>
      <div class="promo-note" style="margin-top:4px">(or pay the difference excluding seafood dish)</div>
    </div>
  </div>

  <section class="welcome">
    <h2 class="section-title" style="left:120px">Welcome to <em>The Golden Lantern</em></h2>
    <div class="welcome-photo" role="img" aria-label="Photo of glazed chicken wings with sesame seeds"></div>
    <div class="welcome-text">
      <p>iste natus error sit voluptatem accusantium doloremque laudantium, totam rem aperiam, eaque ipsa quae ab illo inventore veritatis et quasi architecto beatae vitae dicta sunt explicabo. Nemo enim ipsam voluptatem quia voluptas sit aspernatur aut odit aut fugit, sed quia consequuntur magni dolores eos qui ratione voluptatem sequi nesciunt.</p>
      <p>Neque porro quisquam est, qui dolorem ipsum quia dolor sit amet, consectetur, adipisci velit, sed quia non numquam eius modi tempora incidunt ut labore et dolore magnam aliquam quaerat voluptatem. Ut enim ad minima veniam, quis nostrum exercitationem ullam corporis suscipit laboriosam, nisi ut aliquid ex ea commodi consequatur? Quis autem vel eum iure reprehen-</p>
    </div>
  </section>

  <section class="menu-teaser">
    <h2 class="section-title" style="left:780px">Our Menu</h2>
    <div class="menu-photo" role="img" aria-label="Photo of prawns and noodle dish"></div>
    <div class="menu-text">iste natus error sit voluptatem accusantium doloremque laudantium</div>
    <a class="btn" href="#">View Menu</a>
  </section>

  <footer>
    <div class="footer-rule"></div>
    <div class="copyright">© Copyright 2012 Redfern Web Studio | All Rights Reserved.</div>
    <a class="social" href="#" aria-label="Social link" style="left:941px"></a>
    <a class="social" href="#" aria-label="Social link" style="left:978px"></a>
    <a class="social" href="#" aria-label="Social link" style="left:1015px"></a>
    <a class="social" href="#" aria-label="Social link" style="left:1052px"></a>
  </footer>
</body>
</html>
```